Open Door Dialogues: Classroom and Family Allies building brighter pupil futures.

This is a book that helps to prepare for and hold a standard conference that an educator would have with the parents of the students in the school. It is also about how to have problem-solving conferences around difficult issues using techniques from family therapy. Parent involvement is a key ingredient for student success, but most educators have no training in holding meetings with parents. This book fills that gap.

Target Market(s)

Teachers, principals, counselors, school psychologists, school nurses. Anyone who has conferences with the parents of their students.

Font styles to use
Sans Serif

Colors
85acd3
ffcf3e

Requirements
Must have
• I have several books coming up. I'd like something that could be carried over to the new ones without too many changes. They won't all be about education. I am a psychologist so most of my writings will cover subjects related to emotional intelligence.
Nice to have
• Something dignified that will pop out for those in the schools. I like the combination of a royal blue background with white and gold (not yellow) lettering.
Should not have
• I'd like it to be easy to read. Not too messy or too much stuff on the page.

```html
<!DOCTYPE html>
<html lang="en">
<head>
<meta charset="utf-8">
<title>Open Door Dialogues — Book Cover</title>
<link href="https://fonts.googleapis.com/css2?family=Poppins:wght@200;400;700&display=swap" rel="stylesheet">
<style>
  :root {
    --royal-navy: #1b2163;
    --gold: #d5ae2f;
    --white: #ffffff;
    --muted-blue: #4a5fb0;
    --icon-blue: #3e4fa0;
  }
  html, body {
    margin: 0;
    padding: 0;
    overflow: hidden;
    background: var(--royal-navy);
  }
  .cover {
    position: relative;
    width: 845px;
    height: 1200px;
    background: var(--royal-navy);
    font-family: "Poppins", sans-serif;
    overflow: hidden;
  }
  .icon-ring {
    position: absolute;
    left: 189px;
    top: 155px;
    width: 470px;
    height: 470px;
    border-radius: 50%;
    background: radial-gradient(circle at center,
      rgba(62, 79, 160, 0) 0,
      rgba(62, 79, 160, 0) 62%,
      rgba(62, 79, 160, 0.45) 72%,
      rgba(62, 79, 160, 0.45) 92%,
      rgba(62, 79, 160, 0) 100%);
  }
  .title-light,
  .title-bold,
  .subtitle,
  .author {
    position: absolute;
    left: 0;
    width: 845px;
    margin: 0;
    text-align: center;
    line-height: 1;
    white-space: nowrap;
  }
  .title-light {
    top: 796px;
    font-size: 71px;
    font-weight: 200;
    color: var(--gold);
    letter-spacing: 1px;
  }
  .title-bold {
    top: 875px;
    font-size: 63px;
    font-weight: 700;
    color: var(--gold);
    letter-spacing: 0.5px;
  }
  .subtitle-rule {
    position: absolute;
    left: 69px;
    width: 700px;
    height: 1px;
    background: var(--white);
  }
  .subtitle-rule.top { top: 963px; }
  .subtitle-rule.bottom { top: 1007px; }
  .subtitle {
    top: 972px;
    font-size: 21px;
    font-weight: 400;
    color: var(--white);
  }
  .author {
    top: 1089px;
    font-size: 27px;
    font-weight: 700;
    color: var(--muted-blue);
  }
</style>
</head>
<body>
  <main class="cover">
    <div class="icon-ring" role="img" aria-label="Ring of thin line icons of school items: books, calculator, globe, flasks, pencils, charts and a computer screen"></div>

    <h1 class="title">
      <span class="title-light">OPEN DOOR</span>
      <span class="title-bold">DIALOGUES</span>
    </h1>

    <div class="subtitle-rule top"></div>
    <p class="subtitle">Classroom and Family Allies building brighter pupil futures</p>
    <div class="subtitle-rule bottom"></div>

    <p class="author">Author Name</p>
  </main>
</body>
</html>
```